Dorian Blakely & Morning Lanterns

I need a cd cover designed for a Gospel/Christian Choir. I'm attaching the main picture I want on the cover. This is our single "Lift my heart higher".

Requirements
Must have
• Single name: Lift My Heart Higher

```html
<!DOCTYPE html>
<html lang="en">
<head>
<meta charset="utf-8">
<title>Lift My Heart Higher — Dorian Blakely &amp; Morning Lanterns</title>
<link rel="stylesheet" href="https://fonts.googleapis.com/css2?family=Antonio:wght@100;300&family=Oswald:wght@400&display=swap">
<style>
  :root {
    --ink: #0b0706;
    --gold: #e2b43a;
    --crimson: #b3151b;
    --wine: #8e0f12;
    --paper: #ffffff;
    --ember: #d9782b;
    --glow: #ffd58a;
  }
  html, body {
    margin: 0;
    padding: 0;
    width: 1200px;
    height: 1196px;
    overflow: hidden;
    background: var(--paper);
  }
  .cover {
    position: relative;
    width: 1200px;
    height: 1196px;
    background: var(--paper);
  }
  .cover svg { display: block; }
  .artist-line {
    font-family: "Oswald", "Arial Narrow", sans-serif;
    font-weight: 400;
    fill: var(--paper);
  }
  .single-title {
    font-family: "Antonio", "Arial Narrow", sans-serif;
    font-weight: 100;
    fill: var(--paper);
  }
  .title-joiner {
    font-family: "Antonio", "Arial Narrow", sans-serif;
    font-weight: 300;
    fill: var(--paper);
  }
</style>
</head>
<body>
<div class="cover">
  <svg width="1200" height="1196" viewBox="0 0 1200 1196" xmlns="http://www.w3.org/2000/svg">
    <defs>
      <linearGradient id="portrait-tone" x1="0" y1="0" x2="1" y2="1">
        <stop offset="0" stop-color="#2a140a"/>
        <stop offset="0.35" stop-color="#5a2a10"/>
        <stop offset="0.6" stop-color="#1a0d08"/>
        <stop offset="1" stop-color="#050303"/>
      </linearGradient>
      <radialGradient id="lamp-glow" cx="0.15" cy="0.1" r="0.35">
        <stop offset="0" stop-color="#ffd58a" stop-opacity="0.9"/>
        <stop offset="1" stop-color="#d9782b" stop-opacity="0"/>
      </radialGradient>
      <radialGradient id="wall-glow" cx="0.85" cy="0.15" r="0.5">
        <stop offset="0" stop-color="#d9782b" stop-opacity="0.8"/>
        <stop offset="1" stop-color="#d9782b" stop-opacity="0"/>
      </radialGradient>
    </defs>

    <!-- Portrait panel -->
    <g class="portrait-panel">
      <rect x="0" y="0" width="778" height="1196" fill="var(--ink)"/>
      <g role="img" aria-label="Portrait of the lead singer in a satin suit and tie, leaning on a railing under a warm street lamp at night">
        <rect x="18" y="18" width="742" height="1160" fill="url(#portrait-tone)"/>
        <rect x="18" y="18" width="742" height="1160" fill="url(#wall-glow)"/>
        <rect x="18" y="18" width="742" height="1160" fill="url(#lamp-glow)"/>
      </g>
      <g class="gold-frame" fill="none" stroke="var(--gold)">
        <rect x="12" y="12" width="754" height="1172" stroke-width="5"/>
        <rect x="22" y="22" width="734" height="1152" stroke-width="2"/>
      </g>
      <g class="corner-stripes" stroke="var(--gold)" stroke-width="4">
        <line x1="40" y1="100" x2="120" y2="20"/>
        <line x1="40" y1="130" x2="150" y2="20"/>
        <line x1="40" y1="160" x2="180" y2="20"/>
        <line x1="40" y1="190" x2="210" y2="20"/>
        <line x1="560" y1="1176" x2="740" y2="996"/>
        <line x1="600" y1="1176" x2="740" y2="1036"/>
        <line x1="640" y1="1176" x2="740" y2="1076"/>
        <line x1="680" y1="1176" x2="740" y2="1116"/>
      </g>
    </g>

    <!-- Artist band -->
    <g class="artist-band">
      <rect x="784" y="0" width="48" height="1196" fill="var(--crimson)"/>
      <text class="artist-line" transform="translate(794 12) rotate(90)" font-size="44" textLength="1172" lengthAdjust="spacingAndGlyphs">DORIAN BLAKELY &amp; MORNING LANTERNS</text>
    </g>

    <!-- Title panel -->
    <g class="title-panel">
      <rect x="844" y="0" width="356" height="1196" fill="var(--paper)"/>
      <rect x="852" y="0" width="3" height="1196" fill="var(--wine)"/>
      <rect x="1182" y="0" width="3" height="1196" fill="var(--wine)"/>
      <rect x="864" y="0" width="310" height="1196" fill="var(--wine)"/>
      <text class="single-title" transform="translate(878 0) rotate(90)" font-size="380" textLength="496" lengthAdjust="spacingAndGlyphs">LIFT MY</text>
      <g class="title-joiner-box">
        <rect x="912" y="514" width="228" height="172" fill="none" stroke="var(--paper)" stroke-width="5"/>
        <rect x="926" y="528" width="200" height="144" fill="none" stroke="var(--paper)" stroke-width="2"/>
        <text class="title-joiner" transform="translate(962 548) rotate(90)" font-size="150" textLength="104" lengthAdjust="spacingAndGlyphs">HEART</text>
      </g>
      <text class="single-title" transform="translate(878 702) rotate(90)" font-size="380" textLength="494" lengthAdjust="spacingAndGlyphs">HIGHER</text>
    </g>
  </svg>
</div>
</body>
</html>
```